Wandelow valley aerial works business card size advertising

I’m after a simple design , please see attached photo . Im after the same color green in the photo as the base color and the the little white man but instead of him holding a spanner i would like him to be holding a tv antenna pointing an angle , see attached photo of the antenna , i would like him on the left of the business card and the business name to fit in on the right with the phone number . ( if the antenna idea looks stupid , leave him holding a spanner ) On the reverse side of the card i would like a white background with green writing stating some of the services we provide which are the following .Antenna installations and repairs Wall mounting of tv’s Additional TV outlets Orbix satellite supply and installations Wandelow , Brackenfell , Moravale , Tarrowin , Kelsmoor , Collector , All rural areas All in all i would like the business card to compliment my invoices as pictured “ invoice supplied is a dummy invoice “

wandelow valley aerial works 0491836527

Sans Serif

9bcb3c

• what i ask for in project description

```html
<!DOCTYPE html>
<html lang="en">
<head>
<meta charset="utf-8">
<title>Wandelow Valley Aerial Works – Business Card</title>
<link rel="stylesheet" href="https://fonts.googleapis.com/css2?family=Oswald:wght@500;600&family=Exo+2:wght@600&display=swap">
<style>
  :root {
    --backdrop: #1a1a1a;
    --card: #242424;
    --card-edge: #2c2c2c;
    --green: #9bcb3c;
    --green-soft: rgba(155, 203, 60, 0.55);
    --white: #ffffff;
  }
  * { box-sizing: border-box; margin: 0; padding: 0; }
  html, body {
    width: 1200px; height: 900px; overflow: hidden;
    background: var(--backdrop);
  }
  .canvas {
    position: relative; width: 1200px; height: 900px;
  }
  .card {
    position: absolute; left: 220px; width: 760px; height: 300px;
    background: linear-gradient(135deg, var(--card-edge), var(--card));
    border-bottom: 4px solid var(--green);
    overflow: hidden;
  }
  .card--back { top: 110px; }
  .card--front { top: 450px; }

  .services {
    position: absolute; left: 0; right: 0; top: 112px;
    text-align: center;
    font-family: "Oswald", sans-serif; font-weight: 500;
    color: var(--green); text-transform: uppercase;
    letter-spacing: 0.06em;
  }
  .services__title { font-size: 26px; line-height: 1.25; }
  .services__areas { font-size: 30px; line-height: 1.25; }

  .artwork {
    position: absolute;
    background: linear-gradient(160deg, var(--green), var(--green-soft));
    border-radius: 6px;
    opacity: 0.85;
  }
  .artwork--antenna { left: 250px; top: 26px; width: 320px; height: 84px; }
  .artwork--figure { left: 60px; top: 70px; width: 180px; height: 214px; }

  .brand {
    position: absolute; left: 300px; top: 118px;
    text-transform: uppercase;
  }
  .brand__name {
    font-family: "Oswald", sans-serif; font-weight: 600;
    font-size: 46px; line-height: 1; color: var(--green);
    letter-spacing: 0.05em;
  }
  .brand__tagline {
    font-family: "Oswald", sans-serif; font-weight: 600;
    font-size: 36px; line-height: 1.2; color: var(--green);
    letter-spacing: 0.32em; margin-top: 4px;
  }
  .brand__phone {
    font-family: "Exo 2", sans-serif; font-weight: 600;
    font-size: 50px; line-height: 1.1; color: var(--white);
    letter-spacing: 0.12em; margin-top: 2px;
  }
</style>
</head>
<body>
<main class="canvas">
  <section class="card card--back">
    <div class="services">
      <p class="services__title">Antenna installations Wandelow</p>
      <p class="services__areas">Brackenfell | Moravale | Tarrowin | Kelsmoor</p>
    </div>
  </section>

  <section class="card card--front">
    <div class="artwork artwork--antenna" role="img" aria-label="Green TV antenna illustration held by the figure"></div>
    <div class="artwork artwork--figure" role="img" aria-label="Green pictogram figure with hand on hip holding the antenna mast"></div>
    <div class="brand">
      <p class="brand__name">Wandelow Valley</p>
      <p class="brand__tagline">Aerial Works</p>
      <p class="brand__phone">0491836527</p>
    </div>
  </section>
</main>
</body>
</html>
```